Varga Lillas Physiotherapy Business Card Vienna

We need a business card design for a newly created Physiotherapy company based in Vienna Austria.
We seek a simple, modern, minimalist design without too much color variation. The font should look young/fresh, but definitely not childish or so. Since we are a starting Business, we currently haven't got a logo, if you feel like a logo would fit your design, feel free to use one, but it's not necessary.
Target Market(s)
Healthcare, young and elderly people with mobility issues
Industry/Entity Type
Health And Wellness
Contact Information for Business Card
Name: Lilla Varga
Title description: Physiotherapist
Phone num: +43 664 5290 4816
e-mail: lilla.praxis@brelomail.com
Colors
Designer to choose colors to be used in the design.
Requirements
Must have
- Final design language must be in German, basically, the Title Description needs to be "Physiotherapeutin" the other details remain as in the English Language.
Nice to have
- Simple, modern, minimalist design
Should not have
- too many colors, Obvious use of a skeleton, skull, spline

```html
<!DOCTYPE html>
<html lang="de">
<head>
<meta charset="utf-8">
<title>Lilla Varga – Physiotherapeutin</title>
<link rel="stylesheet" href="https://fonts.googleapis.com/css2?family=Montserrat:wght@300;400;500;900&display=swap">
<style>
  :root {
    --bg: #e2e3e4;
    --lime: #a9bc2f;
    --lime-soft: #b4c640;
    --ink: #232323;
    --paper: #ffffff;
    --white: #ffffff;
  }
  html, body {
    margin: 0;
    width: 1200px;
    height: 1021px;
    overflow: hidden;
    background: var(--bg);
    font-family: "Montserrat", sans-serif;
  }
  .card {
    position: absolute;
    left: 280px;
    width: 640px;
    height: 366px;
    box-shadow: 0 4px 14px rgba(0,0,0,0.18);
    overflow: hidden;
  }
  .card--back { top: 110px; background: var(--lime); }
  .card--front { top: 540px; background: var(--paper); }

  .card__pattern {
    position: absolute;
    inset: 0;
    background: linear-gradient(135deg, var(--lime-soft), var(--lime));
  }
  .back-title {
    position: absolute;
    right: 44px;
    bottom: 42px;
    text-align: right;
    color: var(--white);
    line-height: 0.9;
  }
  .back-title__bold {
    display: block;
    font-weight: 900;
    font-size: 44px;
    letter-spacing: 1px;
  }
  .back-title__light {
    display: block;
    font-weight: 300;
    font-size: 44px;
    letter-spacing: 0.5px;
    margin-right: -6px;
  }

  .name {
    position: absolute;
    left: 52px;
    top: 46px;
    margin: 0;
    font-weight: 900;
    font-size: 56px;
    line-height: 0.86;
    color: var(--ink);
    letter-spacing: 0.5px;
  }
  .role {
    position: absolute;
    left: 52px;
    top: 140px;
    background: var(--lime);
    color: var(--white);
    font-weight: 400;
    font-size: 25px;
    padding: 2px 30px 4px 8px;
    line-height: 1.2;
  }
  .contact {
    position: absolute;
    left: 52px;
    bottom: 48px;
    margin: 0;
    padding: 0;
    list-style: none;
    font-size: 15px;
    color: var(--ink);
    font-weight: 400;
  }
  .contact__item {
    display: flex;
    align-items: center;
    gap: 10px;
    height: 24px;
  }
  .contact__icon { width: 15px; height: 15px; flex: none; }
</style>
</head>
<body>
  <section class="card card--back" aria-label="Rückseite">
    <div class="card__pattern" role="img" aria-label="Monogramm-Muster aus wiederholten Initialen in hellem Grün"></div>
    <div class="back-title">
      <span class="back-title__bold">PHYSIO</span>
      <span class="back-title__light">THERAPEUTIN</span>
    </div>
  </section>

  <section class="card card--front" aria-label="Vorderseite">
    <h1 class="name">LILLA<br>VARGA</h1>
    <div class="role">Physiotherapeutin</div>
    <ul class="contact">
      <li class="contact__item">
        <svg class="contact__icon" viewBox="0 0 24 24" aria-hidden="true">
          <path fill="#a9bc2f" d="M6.6 10.8a15.1 15.1 0 0 0 6.6 6.6l2.2-2.2a1 1 0 0 1 1-.25 11.4 11.4 0 0 0 3.6.57 1 1 0 0 1 1 1V20a1 1 0 0 1-1 1A17 17 0 0 1 3 4a1 1 0 0 1 1-1h3.5a1 1 0 0 1 1 1c0 1.25.2 2.45.57 3.57a1 1 0 0 1-.25 1z"/>
        </svg>
        <span>+43 664 5290 4816</span>
      </li>
      <li class="contact__item">
        <svg class="contact__icon" viewBox="0 0 24 24" aria-hidden="true">
          <rect x="2" y="5" width="20" height="14" fill="none" stroke="#a9bc2f" stroke-width="2.4"/>
          <path d="M2 5l10 8 10-8" fill="none" stroke="#a9bc2f" stroke-width="2.4"/>
        </svg>
        <span>lilla.praxis@brelomail.com</span>
      </li>
    </ul>
  </section>
</body>
</html>
```